Amber Lantern Cafe Business Card

We need a business card design for a new European Cafe. Main menu will be coffee and deserts.

Requirements
Must have
• Logo - 1 of the attached versions
Address - TBA (you can use 487 Morrow Ave Unit 9 for now)
Phone - TBA (you can use 555-238-4176 for now)

```html
<!DOCTYPE html>
<html lang="en">
<head>
<meta charset="utf-8">
<title>Amber Lantern Cafe – Business Card</title>
<link rel="stylesheet" href="https://fonts.googleapis.com/css2?family=Carlito:wght@400;700&display=swap">
<style>
  :root {
    --card-bg: #ffffff;
    --brand-red: #9b1c22;
    --ink: #111111;
    --brand-ink: #2a2522;
  }
  html, body {
    margin: 0;
    padding: 0;
    width: 1200px;
    height: 693px;
    overflow: hidden;
    background: var(--card-bg);
  }
  .card {
    position: relative;
    width: 1200px;
    height: 693px;
    background: var(--card-bg);
    font-family: "Carlito", "Calibri", sans-serif;
    color: var(--ink);
  }
  .brand {
    position: absolute;
    left: 65px;
    top: 71px;
    height: 278px;
    display: flex;
    align-items: center;
    gap: 52px;
  }
  .brand-square {
    width: 283px;
    height: 278px;
    border-radius: 12px;
    background: var(--brand-red);
    flex: none;
  }
  .brand-name {
    font-family: "Carlito", "Calibri", sans-serif;
    font-weight: 400;
    font-size: 84px;
    line-height: 1;
    color: var(--brand-ink);
    white-space: nowrap;
    margin: 0;
  }
  .contact-person,
  .contact-location {
    position: absolute;
    top: 436px;
    margin: 0;
    font-weight: 700;
    font-size: 48px;
    line-height: 68px;
    font-style: normal;
  }
  .contact-person {
    left: 57px;
  }
  .contact-location {
    right: 54px;
    text-align: right;
  }
  .contact-person span,
  .contact-location span {
    display: block;
  }
</style>
</head>
<body>
  <main class="card">
    <header class="brand">
      <div class="brand-square" aria-hidden="true"></div>
      <h1 class="brand-name">Amber Lantern Cafe</h1>
    </header>

    <p class="contact-person">
      <span class="person-name">Daniel Hart</span>
      <span class="person-role">Manager</span>
    </p>

    <address class="contact-location">
      <span class="street">487 Morrow Ave, Unit 9</span>
      <span class="phone">555-238-4176</span>
    </address>
  </main>
</body>
</html>
```